Brantley Fuel Retro Website Design

Have a logo. Need a website design to go along with the logo design. Full Design Specs are here: https://files.quormbex.net/doc/8QwLp2ZtR4vNx7sYh3JkM9aDc5Ub6FgTe1WiO0rVn2X/view

Target Market(s)

Independent Gas Station Owners

Number of Pages Required

1 page

Font styles to use
Sans Serif

Colors

Designer to choose colors to be used in the design.

```html
<!DOCTYPE html>
<html lang="en">
<head>
<meta charset="utf-8">
<title>Brantley Fuel</title>
<link rel="stylesheet" href="https://fonts.googleapis.com/css2?family=Open+Sans:wght@300;400;600&family=Oswald:wght@500;700&display=swap">
<style>
:root{
  --red:#e0231f;
  --nav:#3b2e24;
  --ink:#3a2a1c;
  --text:#5c5650;
  --cream:#f8ecd8;
  --grey:#f2f1ef;
  --testi:#4c3d30;
  --foot:#1d1b19;
  --flourish:#e2d8ca;
  --white:#fff;
}
*{box-sizing:border-box;margin:0;padding:0}
html,body{width:1200px;height:3906px;overflow:hidden}
body{position:relative;font-family:"Open Sans",Arial,sans-serif;color:var(--text);background:var(--white)}
.abs{position:absolute}
.btn-red{position:absolute;background:var(--red);color:#fff;font-size:14px;display:flex;align-items:center;justify-content:center}
.accent{color:var(--red)}

.topbar{left:0;top:0;width:1200px;height:37px;background:var(--nav);z-index:3}
.topbar a{position:absolute;top:9px;color:#eee;font-size:14px;text-decoration:none}
.phone{display:flex;align-items:center;gap:8px}

.brand-ribbon{z-index:4;background:#fff;display:flex;flex-direction:column;align-items:center;padding-top:22px;box-shadow:0 2px 6px rgba(0,0,0,.25)}
.brand-mark{width:54px;height:54px;border-radius:50%;background:#555}
.brand-name{margin-top:8px;font-weight:600;color:var(--ink);letter-spacing:.5px}

.hero{left:0;top:37px;width:1200px;height:709px;background:linear-gradient(100deg,#f3efea 0%,#e2d9cf 45%,#a89684 75%,#7a6755 100%)}
.hero-ground{left:0;top:520px;width:1200px;height:189px;background:linear-gradient(180deg,rgba(120,100,80,.2),#5f4e3e)}
.hero-title{left:76px;top:344px;font-family:"Oswald",Arial,sans-serif;font-weight:700;font-size:27px;line-height:31px;color:var(--ink);text-transform:uppercase;white-space:nowrap;transform:scaleX(.84);transform-origin:left top;letter-spacing:-.2px}
.hero-btn{left:83px;top:463px;width:158px;height:51px;border:1.5px solid #6a5a4c;border-radius:14px;color:var(--ink);font-size:14px;display:flex;align-items:center;justify-content:center}

.about{left:0;top:746px;width:1200px;height:328px;background:var(--grey)}
.about-bg{left:0;top:0;width:1200px;height:328px;background:linear-gradient(180deg,#e8e6e2,#f2f1ef 70%)}
.section-title{position:absolute;left:0;width:1200px;text-align:center;font-weight:300;font-size:30px;color:#333}
.section-sub{position:absolute;text-align:center;font-size:13px;line-height:16px;color:#555}
.rule{position:absolute;height:1px;background:#777}
.about-badge{left:576px;top:30px;width:76px;height:76px;border-radius:50%;background:#fff;border:3px solid #444;display:flex;align-items:center;justify-content:center;font-size:9px;font-weight:600;color:var(--ink);text-align:center;line-height:11px}
.about-text{left:111px;top:164px;width:978px;text-align:center;font-size:13px;line-height:16px;color:#555}

.services{left:0;top:1074px;width:1200px;height:1479px;background:var(--cream)}
.flourish{position:absolute;width:68px;height:22px;border-radius:11px;background:var(--flourish)}
.card{position:absolute;left:114px;width:974px;height:299px;background:#fff}
.card-photo{position:absolute;top:26px;height:244px}
.card-title{position:absolute;font-weight:300;font-size:30px;color:#333}
.card-text{position:absolute;width:400px;font-size:13px;line-height:16px;color:#555}

.why{left:0;top:2553px;width:1200px;height:617px;background:#f4f4f4}
.rod{position:absolute;height:6px;background:#bbb;border-radius:3px}
.rod-end{position:absolute;width:16px;height:16px;border-radius:50%;background:#aaa}
.banner{position:absolute;top:190px;width:285px;height:364px}
.banner-label{position:absolute;left:0;width:285px;top:198px;text-align:center;color:var(--red);font-size:14px}
.banner-text{position:absolute;left:25px;width:235px;top:234px;text-align:center;font-size:12.5px;line-height:16px;color:#666}

.testi{left:0;top:3170px;width:1200px;height:426px;background:var(--testi)}
.testi-bg{left:0;top:0;width:1200px;height:426px;background:linear-gradient(180deg,#54443a,#3e3127)}
.quote{position:absolute;font-family:Georgia,serif;font-size:130px;color:#8a7a6a;line-height:1}
.avatar{position:absolute;border-radius:50%;background:#8f7f70;border:4px solid #fff}
.dots{left:535px;top:3543px;display:flex;gap:7px}
.dots span{width:15px;height:15px;border-radius:50%;border:1.5px solid var(--red)}
.dots span.on{background:var(--red)}

.footer{left:0;top:3596px;width:1200px;height:310px;background:var(--foot)}
.foot-head{position:absolute;top:69px;color:var(--red);font-size:19px}
.foot-list{position:absolute;top:108px;list-style:none;color:#ddd;font-size:14px;line-height:30px}
.foot-list li{display:flex;align-items:center;gap:10px}
.foot-list i{width:8px;height:8px;border-radius:50%;background:var(--red);display:inline-block}
</style>
</head>
<body>

<nav class="abs topbar">
  <a style="left:391px">Home</a>
  <a style="left:480px">About us</a>
  <a style="left:583px">Services</a>
  <a style="left:680px">Why choose us</a>
  <a style="left:818px">Contact</a>
  <a class="phone" style="left:983px">
    <svg width="14" height="14" viewBox="0 0 24 24"><path fill="#e0231f" d="M6.6 10.8a15 15 0 0 0 6.6 6.6l2.2-2.2c.3-.3.7-.4 1-.2 1.1.4 2.3.6 3.6.6.6 0 1 .4 1 1V20c0 .6-.4 1-1 1A17 17 0 0 1 3 4c0-.6.4-1 1-1h3.5c.6 0 1 .4 1 1 0 1.3.2 2.5.6 3.6.1.3 0 .7-.2 1z"/></svg>
    100 555 0142
  </a>
</nav>

<div class="abs brand-ribbon" style="left:76px;top:0;width:132px;height:152px;clip-path:polygon(0 0,100% 0,100% 100%,50% 82%,0 100%)">
  <div class="brand-mark"></div>
  <div class="brand-name" style="font-size:13px">BRANTLEY FUEL</div>
</div>

<section class="abs hero" role="img" aria-label="Sepia photo of an oil pumpjack beside a shrub in an open field">
  <div class="abs hero-ground"></div>
</section>
<h1 class="abs hero-title">We have all types of incomes that come<br>in here, but for the most part it is hard<br>working, middle income males.</h1>
<a class="abs hero-btn">Read more</a>

<section class="abs about">
  <div class="abs about-bg" role="img" aria-label="Faded photo of a vintage fuel station"></div>
  <div class="rule" style="left:279px;top:58px;width:278px"></div>
  <div class="rule" style="left:675px;top:58px;width:278px"></div>
  <div class="abs about-badge">BRANTLEY<br>FUEL</div>
  <h2 class="section-title" style="top:112px">About <span class="accent">Us</span></h2>
  <p class="abs about-text">Lorem Ipsum is simply dummy text of the printing and typesetting industry. Lorem Ipsum has been the industry's standard dummy text ever since the 1500s, when an unknown printer took a galley of type and scrambled it to make a type specimen book. It has survived not only five centuries, but also the leap into electronic typesetting, remaining essentially unchanged. It was popularised in the 1960s with the release of Letraset sheets containing Lorem Ipsum passages, and more recently with desktop publishing software like Aldus PageMaker including versions of Lorem Ipsum</p>
  <a class="btn-red" style="left:551px;top:254px;width:132px;height:33px">Read more</a>
</section>

<section class="abs services">
  <div class="flourish" style="left:436px;top:52px" role="img" aria-label="Decorative scroll flourish"></div>
  <div class="flourish" style="left:710px;top:52px" role="img" aria-label="Decorative scroll flourish"></div>
  <h2 class="section-title" style="top:42px">Our <span class="accent">Services</span></h2>
  <p class="section-sub" style="left:400px;width:440px;top:96px">We have all types of incomes that come in here, but for the most part it is hard working, middle income males.</p>

  <article class="card" style="top:167px">
    <div class="card-photo" style="left:27px;width:475px;background:linear-gradient(180deg,#d8d2c8,#8c8478)" role="img" aria-label="Photo of a fuel tanker truck"></div>
    <h3 class="card-title" style="left:529px;top:33px">Fuel <span class="accent">Delivery</span></h3>
    <p class="card-text" style="left:529px;top:97px">Brantley Fuel provides fuel delivery for independent gas stations, convenience stores, construction sites or any other commercial need.  If you are looking for gasoline, high sulfer diesel fuel, farm diesel or other bulk fuel delivered to your business, we will take care of you!</p>
    <a class="btn-red" style="left:530px;top:210px;width:144px;height:41px">Read more</a>
  </article>

  <article class="card" style="top:482px">
    <h3 class="card-title" style="left:27px;top:48px;color:var(--red)">Oil</h3>
    <p class="card-text" style="left:27px;top:104px;width:445px">Looking for speciality auto, tractor, tractor trailer, aviation or other commercial oils and lubricants Brantley Fuel can help!  Just call one of our customer oriented staff and we will get what you need quick!  We have a complete line of aviation oils and lubricants as well as gear lubricants, greases, oils and more!</p>
    <a class="btn-red" style="left:27px;top:213px;width:144px;height:41px">Read more</a>
    <div class="card-photo" style="left:502px;width:443px;background:linear-gradient(135deg,#6e6860,#bdb6ac 50%,#4a453f)" role="img" aria-label="Photo of motor oil pouring from a bottle"></div>
  </article>

  <article class="card" style="top:799px">
    <div class="card-photo" style="left:27px;width:475px;background:linear-gradient(180deg,#9e968a,#cfc8bc 60%,#877f73)" role="img" aria-label="Photo of farm fuel storage tanks"></div>
    <h3 class="card-title" style="left:529px;top:48px">Farm <span class="accent">Fuel</span></h3>
    <p class="card-text" style="left:529px;top:109px">Looking for gasoline, diesel red diesel off road fuel or farm diesel?  We can deliver straight to your farm!  We can setup your farm tanks, take care of EPA containment and deliver fuel when you need it!</p>
    <a class="btn-red" style="left:530px;top:204px;width:144px;height:41px">Read more</a>
  </article>

  <article class="card" style="top:1118px">
    <h3 class="card-title" style="left:27px;top:57px">Cargo <span class="accent">Containers</span></h3>
    <p class="card-text" style="left:27px;top:118px;width:450px">Want to purchase or lease a storage container, we have what you need! We can deliver or move storage containers to your home, business, construction site or any you need one!</p>
    <a class="btn-red" style="left:27px;top:195px;width:144px;height:41px">Read more</a>
    <div class="card-photo" style="left:502px;width:443px;background:linear-gradient(180deg,#e8e2d8,#9a8f80 70%,#7d7366)" role="img" aria-label="Photo of stacked cargo containers"></div>
  </article>
</section>

<section class="abs why">
  <div class="flourish" style="left:426px;top:48px;background:#e4e2de" role="img" aria-label="Decorative scroll flourish"></div>
  <div class="flourish" style="left:718px;top:48px;background:#e4e2de" role="img" aria-label="Decorative scroll flourish"></div>
  <h2 class="section-title" style="top:38px">Why <span class="accent">Choose Us</span></h2>
  <p class="section-sub" style="left:430px;width:370px;top:92px">We have all types of incomes that come in here, but for the most part it is hard working, middle income males.</p>
  <div class="rod" style="left:110px;top:159px;width:980px"></div>
  <div class="rod-end" style="left:104px;top:154px"></div>
  <div class="rod-end" style="left:1080px;top:154px"></div>

  <div class="banner" style="left:144px">
    <svg width="285" height="364" viewBox="0 0 285 364"><path d="M0 0h285v364l-142-60L0 364z" fill="#fff"/><rect x="22" y="0" width="18" height="24" fill="#fff" stroke="#ccc"/><circle cx="31" cy="12" r="4" fill="#bbb"/><rect x="245" y="0" width="18" height="24" fill="#fff" stroke="#ccc"/><circle cx="254" cy="12" r="4" fill="#bbb"/><path d="M142 32c-12 30-45 60-45 90a45 45 0 0 0 90 0c0-30-33-60-45-90z" fill="#fff" stroke="#ccc" stroke-width="2"/><path d="M124 115h10v28h-10zM138 143v-28l8-16c4 0 6 3 5 7l-2 9h12c4 0 6 3 5 6l-4 16c-1 4-3 6-6 6z" fill="#e0231f"/></svg>
    <div class="banner-label">Quality Work</div>
    <p class="banner-text">Lorem Ipsum is simply dummy text of the printing and typesetting industry.</p>
  </div>
  <div class="banner" style="left:461px">
    <svg width="285" height="364" viewBox="0 0 285 364"><path d="M0 0h285v364l-142-60L0 364z" fill="#fff"/><rect x="22" y="0" width="18" height="24" fill="#fff" stroke="#ccc"/><circle cx="31" cy="12" r="4" fill="#bbb"/><rect x="245" y="0" width="18" height="24" fill="#fff" stroke="#ccc"/><circle cx="254" cy="12" r="4" fill="#bbb"/><path d="M142 32c-12 30-45 60-45 90a45 45 0 0 0 90 0c0-30-33-60-45-90z" fill="#fff" stroke="#ccc" stroke-width="2"/><path d="M142 98l22 8v16c0 14-10 24-22 28-12-4-22-14-22-28v-16z" fill="#e0231f"/><path d="M132 124l7 7 13-14" fill="none" stroke="#fff" stroke-width="4"/></svg>
    <div class="banner-label">Safety</div>
    <p class="banner-text">Lorem Ipsum is simply dummy text of the printing and typesetting industry.</p>
  </div>
  <div class="banner" style="left:780px">
    <svg width="285" height="364" viewBox="0 0 285 364"><path d="M0 0h285v364l-142-60L0 364z" fill="#fff"/><rect x="22" y="0" width="18" height="24" fill="#fff" stroke="#ccc"/><circle cx="31" cy="12" r="4" fill="#bbb"/><rect x="245" y="0" width="18" height="24" fill="#fff" stroke="#ccc"/><circle cx="254" cy="12" r="4" fill="#bbb"/><path d="M142 32c-12 30-45 60-45 90a45 45 0 0 0 90 0c0-30-33-60-45-90z" fill="#fff" stroke="#ccc" stroke-width="2"/><path d="M133 125l-7 26 9-4 5 8 4-20zM151 125l7 26-9-4-5 8-4-20z" fill="#e0231f"/><circle cx="142" cy="115" r="16" fill="#e0231f"/><circle cx="142" cy="115" r="9" fill="#fff"/></svg>
    <div class="banner-label">Experience</div>
    <p class="banner-text">Lorem Ipsum is simply dummy text of the printing and typesetting industry.</p>
  </div>
</section>

<section class="abs testi">
  <div class="abs testi-bg" role="img" aria-label="Dark faded photo of a vintage fuel station"></div>
  <h2 class="section-title" style="top:32px;color:#eee">What our clients say</h2>
  <div class="rod" style="left:414px;top:89px;width:429px;background:#999"></div>
  <div class="rod-end" style="left:406px;top:84px;background:#999"></div>
  <div class="rod-end" style="left:836px;top:84px;background:#999"></div>
  <div class="quote" style="left:446px;top:118px">&ldquo;</div>
  <div class="quote" style="left:776px;top:328px">&rdquo;</div>
  <svg class="abs" style="left:112px;top:180px" width="26" height="50" viewBox="0 0 26 50"><path d="M24 2L2 25l22 23" fill="none" stroke="#eee" stroke-width="2"/></svg>
  <svg class="abs" style="left:1064px;top:180px" width="26" height="50" viewBox="0 0 26 50"><path d="M2 2l22 23L2 48" fill="none" stroke="#eee" stroke-width="2"/></svg>
  <div class="avatar" style="left:342px;top:196px;width:48px;height:48px;border-width:2px" role="img" aria-label="Client portrait"></div>
  <div class="avatar" style="left:848px;top:203px;width:48px;height:48px;border-width:2px" role="img" aria-label="Client portrait"></div>
  <div class="avatar" style="left:548px;top:151px;width:118px;height:118px" role="img" aria-label="Portrait of client Marcus Dell"></div>
  <div class="abs" style="left:687px;top:200px;color:#eee;font-size:10px;font-weight:600">Marcus Dell<br><span style="font-weight:400">USA</span></div>
  <p class="abs" style="left:268px;top:282px;width:696px;text-align:center;color:#eee;font-size:13px;line-height:16px">Lorem Ipsum is simply dummy text of the printing and typesetting industry. Lorem Ipsum has been the industry's standard dummy text ever since the 1500s,Lorem Ipsum is simply dummy text of the printing and typesetting industry. Lorem Ipsum has been the industry's standard dummy text ever since the 1500s,</p>
</section>
<div class="abs dots"><span></span><span></span><span></span><span></span><span></span><span></span><span class="on"></span><span></span><span></span></div>

<footer class="abs footer">
  <div class="abs" style="left:0;top:0;width:1200px;height:310px;background:linear-gradient(90deg,#1d1b19 55%,#2a2622)" role="img" aria-label="Faint silhouette of an oil pumpjack"></div>
  <div class="abs brand-ribbon" style="left:114px;top:-13px;width:202px;height:247px;padding-top:36px;clip-path:polygon(0 0,100% 0,100% 100%,50% 84%,0 100%)">
    <div class="brand-mark" style="width:90px;height:90px"></div>
    <div class="brand-name" style="font-size:19px">BRANTLEY FUEL</div>
  </div>
  <h4 class="foot-head" style="left:441px;font-weight:400">Company</h4>
  <ul class="foot-list" style="left:444px"><li>Home</li><li>About us</li><li>Services</li><li>Why choose us</li><li>Resources</li></ul>
  <h4 class="foot-head" style="left:675px;font-weight:400">Contact Us</h4>
  <ul class="foot-list" style="left:675px"><li><i></i>Friendwall</li><li><i></i>Chirpline</li><li><i></i>Snapgrid</li></ul>
  <h4 class="foot-head" style="left:902px;font-weight:400">Newsletter Subscribe</h4>
  <p class="abs" style="left:906px;top:112px;width:190px;color:#ddd;font-size:13px;line-height:15px">Our company that has been around since 1966.</p>
  <div class="abs" style="left:907px;top:153px;width:138px;height:24px;background:#fff;font-size:9px;color:#999;padding:6px 6px">Email</div>
  <div class="abs" style="left:1047px;top:153px;width:41px;height:24px;background:var(--red);color:#fff;font-size:9px;display:flex;align-items:center;justify-content:center">Go</div>
  <p class="abs" style="left:132px;top:266px;color:var(--red);font-size:10px">&copy; 2019 Brantley Fuel All rights reserved.</p>
</footer>

</body>
</html>
```